HOLLOWBRIM BASH 2014 - Halloween Party

I need a 8.5x11 poster that can also be a jpeg for facebook and run as a display ad in print. I would like a facebook cover and profile picture that matches the poster. This is our 8th annual Halloween costume party and is our biggest event of the year.

Copy is as follows: (no particular order

8th Annual HOLLOWBRIM BASH
Halloween Costume Party
FRIDAY October 31st (need to emphasize date, usually I do it on Saturday.)
$400 in CASH PRIZES awarded at 9pm AND Midnight
DJ 7pm-2am in the tavern
Live music by VELVET RAVENS in the back room. 9pm.
Drink Specials, Munchies
$5 cover in advance, $10 at the door.
Cedarfield Lodge Inn, 4185 County Road 61, Hillsdale, NY

Target Market(s)

We are a bar and we have live music and a DJ for this party and are awarding for prizes for the best costumes (and other costumer categories.)

Industry/Entity Type

House

Font styles to use
Other font styles liked:
• halloween, spooky but readable

Requirements
Must have
• Must communicate the details clearly, be able to read from a distance. Due to the amount of Information we need to convey, I am willng to go 8x14 poster size. The emphasis should really be on "Hollowbrim Bash". "8th annual" is not very important and should be weighted less than Hollowbrim Bash.
Should not have
• shouldn't be too scary. I've had shop owners tell me that some are too scary to hang in their stores.

```html
<!DOCTYPE html>
<html lang="en">
<head>
<meta charset="utf-8">
<title>Hollowbrim Bash – Halloween Costume Party</title>
<link rel="stylesheet" href="https://fonts.googleapis.com/css2?family=Creepster&family=Bree+Serif&family=Josefin+Sans:ital,wght@1,600&display=swap">
<style>
  :root {
    --blood-pink: #e9576a;
    --pink-soft: #f06b7c;
    --ink: #1b1416;
    --night-deep: #0b1016;
    --night-mid: #26303a;
    --cloud-grey: #56606a;
    --window-glow: #e8a23a;
    --house-shadow: #1a1715;
    --label-white: #f2f2f2;
  }
  html, body {
    margin: 0;
    padding: 0;
    overflow: hidden;
    background: var(--night-deep);
  }
  .poster {
    position: relative;
    width: 686px;
    height: 1200px;
    overflow: hidden;
    background: var(--night-deep);
    color: var(--blood-pink);
    text-align: center;
  }
  .sky {
    position: absolute;
    inset: 0;
    background:
      radial-gradient(ellipse 60% 30% at 50% 58%, rgba(120,135,140,0.45), transparent 70%),
      radial-gradient(ellipse 55% 22% at 30% 22%, rgba(110,120,128,0.55), transparent 70%),
      radial-gradient(ellipse 50% 20% at 80% 38%, rgba(90,100,108,0.5), transparent 70%),
      linear-gradient(180deg, var(--night-deep) 0%, var(--night-mid) 35%, var(--cloud-grey) 55%, var(--night-mid) 72%, var(--night-deep) 100%);
  }
  .haunted-house {
    position: absolute;
    left: 0;
    right: 0;
    top: 860px;
    height: 340px;
    background:
      radial-gradient(ellipse 28% 35% at 52% 55%, rgba(232,162,58,0.35), transparent 70%),
      radial-gradient(ellipse 45% 60% at 50% 60%, #3a3026 0%, var(--house-shadow) 60%, transparent 100%),
      linear-gradient(180deg, transparent 0%, rgba(10,8,8,0.7) 70%, #0d0a09 100%);
  }
  .line { position: absolute; left: 0; right: 0; margin: 0; line-height: 1; white-space: nowrap; }
  .line.offset { left: 56px; }
  .annual {
    top: 22px;
    font-family: "Creepster", system-ui, sans-serif;
    font-size: 34px;
    line-height: 1.05;
    letter-spacing: 1px;
  }
  .title {
    font-family: "Creepster", system-ui, sans-serif;
    color: var(--pink-soft);
    text-shadow: 0 2px 8px rgba(0,0,0,0.5);
  }
  .title-top { top: 172px; font-size: 120px; letter-spacing: 1px; }
  .title-bottom { top: 282px; font-size: 150px; letter-spacing: 4px; }
  .party-label {
    top: 452px;
    font-family: "Josefin Sans", system-ui, sans-serif;
    font-style: italic;
    font-weight: 600;
    font-size: 19px;
    letter-spacing: 1.5px;
    color: var(--label-white);
    display: flex;
    justify-content: center;
    align-items: center;
    gap: 8px;
  }
  .party-label .dot {
    width: 12px; height: 12px; border-radius: 50%;
    background: var(--label-white);
    display: inline-block;
  }
  .date {
    top: 492px;
    font-family: "Creepster", system-ui, sans-serif;
    font-size: 76px;
  }
  .date small { font-size: 40px; }
  .slab { font-family: "Bree Serif", Georgia, serif; font-weight: 400; text-transform: uppercase; }
  .prize-amount { top: 572px; font-size: 92px; }
  .prize-label { top: 656px; font-size: 42px; }
  .prize-times { top: 702px; font-size: 22px; }
  .extras { top: 746px; font-size: 27px; }
  .munchies { top: 772px; font-size: 40px; }
  .cover-advance { top: 812px; font-size: 20px; }
  .cover-door { top: 834px; font-size: 20px; }
  .bubbles { position: absolute; inset: 0; }
  .bubble-text {
    position: absolute;
    font-family: "Creepster", system-ui, sans-serif;
    color: var(--ink);
    line-height: 0.95;
    text-align: center;
  }
  .bubble-dj { left: 38px; top: 806px; width: 170px; font-size: 26px; transform: rotate(-8deg); }
  .bubble-dj .big { font-size: 42px; }
  .bubble-band { left: 508px; top: 748px; width: 134px; font-size: 20px; transform: rotate(6deg); }
  .bubble-band .time { font-size: 30px; }
  .address {
    top: 1148px;
    font-family: "Bree Serif", Georgia, serif;
    font-size: 18px;
    line-height: 1.15;
  }
</style>
</head>
<body>
  <main class="poster">
    <div class="sky" role="img" aria-label="Dark cloudy night sky"></div>
    <div class="haunted-house" role="img" aria-label="Haunted house with glowing windows among bare trees and flying bats"></div>

    <p class="line annual">8TH<br>ANNUAL</p>
    <h1 class="line title title-top">HOLLOWBRIM</h1>
    <p class="line title title-bottom">BASH</p>

    <p class="line party-label"><span class="dot"></span>HALLOWEEN COSTUME PARTY<span class="dot"></span></p>

    <p class="line date">FRIDAY <small>oct.</small>31<small>ST</small></p>

    <p class="line slab prize-amount">$400</p>
    <p class="line offset slab prize-label">Cash Prizes</p>
    <p class="line offset slab prize-times">At 9pm and Midnight</p>

    <p class="line offset slab extras">Drink Specials,</p>
    <p class="line offset slab munchies">Munchies</p>
    <p class="line offset slab cover-advance">$5 Cover in Advance</p>
    <p class="line offset slab cover-door">$10 at the Door</p>

    <svg class="bubbles" width="686" height="1200" viewBox="0 0 686 1200" aria-hidden="true">
      <g fill="var(--blood-pink)">
        <path d="M34 840 C28 800 70 782 120 786 C180 790 214 812 212 848 C210 885 168 905 120 902 C70 899 40 880 34 840 Z"/>
        <path d="M150 898 C160 925 140 945 165 965 C185 980 200 990 196 996 C185 985 160 975 148 955 C135 935 150 918 140 900 Z"/>
        <path d="M500 790 C496 752 540 730 585 733 C630 736 652 765 649 800 C646 835 612 852 575 850 C530 848 503 825 500 790 Z"/>
        <path d="M548 846 C530 870 520 860 515 880 C510 896 500 904 492 906 C500 896 500 878 510 862 C520 850 530 846 540 842 Z"/>
      </g>
    </svg>

    <div class="bubble-text bubble-dj">7PM-2AM<br><span class="big">DJ</span> IN THE<br>TAVERN</div>
    <div class="bubble-text bubble-band"><span class="time">9PM</span><br>VELVET RAVENS<br>LIVE</div>

    <p class="line address">CEDARFIELD LODGE INN, 4185<br>COUNTY ROAD 61, HILLSDALE, NY</p>
  </main>
</body>
</html>
```